Life Coaching and Personal Development Business. Needs Business Card with Logo

We are a Life Coaching and Personal Development Business based in Melbourne, Victoria. We specialise in assisting Individuals who find themselves at cross roads due to career, relationships or just life experiences that are preventing them from having extraordinary lives in happiness, finance or relationships or just being disconnected from a sense of purpose. Our motto is "we help you get there".
Updates

Reason: I am awaiting final concepts from a couple of designers

Reason: Deadline passed so now would like to see more options.

Target Market(s)

Individuals who want to move through the cross roads and who are aware that they require help to do so. They are seeking happy, for filing lives through all aspects career, relationships, family and finance

Industry/Entity Type

Finance

Font styles to use
Script

Requirements
Must have
• logo which is representative of moving forward
Business Name: RV Bright Harbour
ABN: 5836071924

I do not have a preference with colour but I do not want red orange or green

Should not have
• The card must not be to busy.

```html
<!DOCTYPE html>
<html lang="en">
<head>
<meta charset="utf-8">
<title>RV Bright Harbour – Business Card</title>
<link href="https://fonts.googleapis.com/css2?family=Arimo:wght@400;700&family=Dancing+Script:wght@600;700&display=swap" rel="stylesheet">
<style>
  :root {
    --backdrop: #dcdcdc;
    --ink: #0c0c0c;
    --paper: #ffffff;
    --accent: #2f62b0;
    --accent-deep: #1f3f78;
    --text-light: #ffffff;
    --text-dark: #111111;
  }
  * { box-sizing: border-box; margin: 0; padding: 0; }
  html, body {
    width: 1200px; height: 985px; overflow: hidden;
    background: var(--backdrop);
    font-family: "Arimo", Arial, sans-serif;
  }
  .sheet { position: relative; width: 1200px; height: 985px; }
  .card {
    position: absolute; left: 250px; width: 700px; height: 400px;
    border-radius: 28px; overflow: hidden;
    box-shadow: 0 10px 28px rgba(0,0,0,.22);
  }

  /* Back face */
  .card--back { top: 50px; background: var(--ink); }
  .card--back .brand {
    position: absolute; left: 90px; top: 70px;
    display: flex; align-items: center; gap: 30px;
  }
  .brand__dot {
    flex: none; width: 190px; height: 190px; border-radius: 50%;
    background: var(--accent);
  }
  .card--back .brand__name {
    color: var(--text-light); font-weight: 700; font-size: 50px; line-height: 1.1;
  }
  .card--back .band {
    position: absolute; left: 0; right: 0; bottom: 0; height: 64px;
    background: var(--accent-deep);
  }
  .card--back .band__rule {
    position: absolute; left: 0; right: 0; top: 24px; height: 3px;
    background: var(--text-light);
  }
  .card--back .tagline {
    position: absolute; left: 160px; top: 2px;
    padding: 0 14px; background: var(--accent-deep);
    color: var(--text-light); font-family: "Dancing Script", cursive;
    font-weight: 700; font-size: 32px; line-height: 48px; white-space: nowrap;
  }

  /* Front face */
  .card--front { top: 520px; background: var(--paper); }
  .card--front .wave { position: absolute; inset: 0; }
  .card--front .brand {
    position: absolute; left: 300px; top: 38px;
    display: flex; align-items: center; gap: 18px;
  }
  .card--front .brand__dot { width: 110px; height: 110px; }
  .card--front .brand__name {
    color: var(--text-dark); font-weight: 700; font-size: 34px; line-height: 1.1;
  }
  .holder {
    position: absolute; left: 40px; top: 178px;
    color: var(--text-light); font-family: "Dancing Script", cursive;
    font-weight: 700; font-size: 36px; white-space: nowrap;
  }
  .contacts {
    position: absolute; left: 40px; top: 258px; list-style: none;
    color: var(--text-light); font-weight: 700; font-size: 21px; line-height: 1.55;
    white-space: nowrap;
  }
</style>
</head>
<body>
<main class="sheet">

  <section class="card card--back" aria-label="Card back">
    <div class="brand">
      <span class="brand__dot"></span>
      <span class="brand__name">RV Bright<br>Harbour</span>
    </div>
    <div class="band">
      <div class="band__rule"></div>
      <p class="tagline">"We help you get there"</p>
    </div>
  </section>

  <section class="card card--front" aria-label="Card front">
    <svg class="wave" viewBox="0 0 700 400" preserveAspectRatio="none" aria-hidden="true">
      <path d="M0 150 C150 110 260 150 380 250 C470 325 580 350 700 340 L700 400 L0 400 Z" fill="var(--accent-deep)"/>
      <path d="M0 162 C150 122 255 166 370 262 C460 335 560 364 700 358 L700 400 L0 400 Z" fill="var(--ink)"/>
      <path d="M0 382 L700 382 L700 400 L0 400 Z" fill="var(--accent-deep)"/>
    </svg>
    <div class="brand">
      <span class="brand__dot"></span>
      <span class="brand__name">RV Bright<br>Harbour</span>
    </div>
    <p class="holder">Jordan Pellow</p>
    <ul class="contacts">
      <li>- P.O. Box 4162, Ashbury VIC 3147</li>
      <li>- 0412 583 906</li>
      <li>- jordan@brightharbour.com.au</li>
    </ul>
  </section>

</main>
</body>
</html>
```